Bref créative
Turnip Cuddler LLC
Embracing More Plant-Based Eating for Everyone
Bright & Fun-filled
Paula J. Mercer
Health & Wellness Coach, NQRS Certified
418 Marlow Ln.
Georgetown, KY 40871
theturnipcuddler@mailnest.example
www.turnipcuddler.example
http://twitter.com/TurnipCuddler
I do not want to have the address on the card.
Just the logo?

```html
<!DOCTYPE html>
<html lang="en">
<head>
<meta charset="utf-8">
<title>Turnip Cuddler Stationery</title>
<link href="https://fonts.googleapis.com/css2?family=Open+Sans:wght@400;700&display=swap" rel="stylesheet">
<style>
:root{
  --bg:#1c1c1e;
  --paper:#ffffff;
  --green:#3f9a2c;
  --green-light:#7cc142;
  --green-dark:#24701d;
  --brown:#6b4a2e;
  --ink:#4a4a4a;
  --faint:#e6e6e6;
}
*{box-sizing:border-box;margin:0;padding:0}
html,body{width:1200px;height:314px;overflow:hidden;background:var(--bg);font-family:"Open Sans",Arial,sans-serif}
.stage{position:relative;width:1200px;height:314px}
.item{position:absolute;background:var(--paper);overflow:hidden;box-shadow:0 3px 8px rgba(0,0,0,.6)}
.wordmark{display:flex;align-items:center;gap:4px;color:var(--green);font-weight:700;white-space:nowrap}
.wordmark .mark{border-radius:50%;background:var(--green);flex:none}
.band{position:absolute;left:0;bottom:0;width:100%}
.tiny{font-size:4px;color:var(--ink);line-height:1.4}

.brand-lockup{position:absolute;left:30px;top:100px}
.brand-lockup .wordmark{font-size:21px}
.brand-lockup .mark{width:24px;height:24px}
.brand-lockup .tagline{font-size:6px;color:#bbb;margin:3px 0 0 28px}

.card-front .wordmark{position:absolute;left:8px;top:10px;font-size:9px}
.card-front .mark{width:12px;height:12px}
.card-front .contact{position:absolute;left:60px;top:12px;font-size:3.5px}
.card-symbol{display:flex;align-items:center;justify-content:center}
.card-symbol .mark{width:26px;height:26px;border-radius:50%;background:var(--green)}
.card-green{background:linear-gradient(180deg,var(--green-light),var(--green-dark))}
.card-green .mark{background:var(--paper)}

.letterhead .wordmark{position:absolute;left:12px;top:12px;font-size:10px}
.letterhead .mark{width:12px;height:12px}
.letterhead .contact{position:absolute;right:14px;top:12px;font-size:3.5px;text-align:left}
.letterhead .watermark{position:absolute;left:50%;top:38%;transform:translate(-50%,-50%);width:70px;height:70px;border-radius:50%;background:var(--faint)}
.letterhead .footer{position:absolute;bottom:6px;width:100%;text-align:center;font-size:3.5px;color:#fff}

.comp .wordmark{position:absolute;left:8px;top:10px;font-size:8px}
.comp .mark{width:10px;height:10px}
.comp .watermark{position:absolute;left:50%;top:42%;transform:translate(-50%,-50%);width:34px;height:34px;border-radius:50%;background:var(--faint)}

.envelope-back .flap{position:absolute;left:0;top:0;width:100%;height:100%}
.envelope-front .wordmark{position:absolute;left:10px;top:8px;font-size:8px}
.envelope-front .mark{width:10px;height:10px}
</style>
</head>
<body>
<main class="stage">

  <div class="brand-lockup">
    <div class="wordmark"><span class="mark"></span>Turnip Cuddler</div>
    <p class="tagline">Embracing More Plant-Based Eating</p>
  </div>

  <!-- business cards -->
  <section class="item card-front" style="left:28px;top:186px;width:115px;height:72px">
    <div class="wordmark"><span class="mark"></span>Turnip Cuddler</div>
    <svg class="band" viewBox="0 0 115 16" height="16" preserveAspectRatio="none"><path d="M0 8 Q60 0 115 6 V16 H0Z" fill="var(--green)"/><path d="M0 8 Q60 0 115 6" stroke="var(--brown)" stroke-width="1.2" fill="none"/></svg>
  </section>
  <section class="item card-front" style="left:150px;top:186px;width:115px;height:72px">
    <div class="wordmark" style="font-size:7px"><span class="mark" style="width:9px;height:9px"></span>Turnip Cuddler</div>
    <div class="contact tiny" style="top:26px;left:8px">Paula J. Mercer<br>Health &amp; Wellness Coach, NQRS Certified<br>theturnipcuddler@mailnest.example<br>www.turnipcuddler.example</div>
    <svg class="band" viewBox="0 0 115 16" height="16" preserveAspectRatio="none"><path d="M0 8 Q60 0 115 6 V16 H0Z" fill="var(--green)"/><path d="M0 8 Q60 0 115 6" stroke="var(--brown)" stroke-width="1.2" fill="none"/></svg>
  </section>
  <section class="item card-symbol" style="left:28px;top:266px;width:115px;height:44px">
    <span class="mark"></span>
  </section>
  <section class="item card-symbol card-green" style="left:150px;top:266px;width:115px;height:44px">
    <span class="mark"></span>
  </section>

  <!-- letterheads -->
  <section class="item letterhead" style="left:288px;top:12px;width:180px;height:288px">
    <div class="wordmark"><span class="mark"></span>Turnip Cuddler</div>
    <div class="contact tiny">418 Marlow Ln.<br>Georgetown, KY 40871<br>www.turnipcuddler.example</div>
    <div class="watermark"></div>
    <svg class="band" viewBox="0 0 180 22" height="22" preserveAspectRatio="none"><path d="M0 12 Q90 0 180 10 V22 H0Z" fill="var(--green)"/><path d="M0 12 Q90 0 180 10" stroke="var(--brown)" stroke-width="1.5" fill="none"/></svg>
    <div class="footer">theturnipcuddler@mailnest.example</div>
  </section>
  <section class="item letterhead" style="left:492px;top:12px;width:190px;height:288px">
    <div class="wordmark"><span class="mark"></span>Turnip Cuddler</div>
    <div class="watermark"></div>
    <svg class="band" viewBox="0 0 190 22" height="22" preserveAspectRatio="none"><path d="M0 12 Q95 0 190 10 V22 H0Z" fill="var(--green)"/><path d="M0 12 Q95 0 190 10" stroke="var(--brown)" stroke-width="1.5" fill="none"/></svg>
    <div class="footer">www.turnipcuddler.example</div>
  </section>

  <!-- compliment cards -->
  <section class="item comp" style="left:700px;top:77px;width:152px;height:90px">
    <div class="wordmark"><span class="mark"></span>Turnip Cuddler</div>
    <div class="watermark"></div>
    <svg class="band" viewBox="0 0 152 18" height="18" preserveAspectRatio="none"><path d="M0 10 Q76 0 152 8 V18 H0Z" fill="var(--green)"/><path d="M0 10 Q76 0 152 8" stroke="var(--brown)" stroke-width="1.2" fill="none"/></svg>
  </section>
  <section class="item comp" style="left:700px;top:175px;width:152px;height:96px">
    <div class="wordmark"><span class="mark"></span>Turnip Cuddler</div>
    <div class="watermark"></div>
    <svg class="band" viewBox="0 0 152 18" height="18" preserveAspectRatio="none"><path d="M0 10 Q76 0 152 8 V18 H0Z" fill="var(--green)"/><path d="M0 10 Q76 0 152 8" stroke="var(--brown)" stroke-width="1.2" fill="none"/></svg>
  </section>

  <!-- envelopes -->
  <section class="item envelope-back" style="left:868px;top:79px;width:308px;height:113px">
    <svg class="flap" viewBox="0 0 308 113" preserveAspectRatio="none">
      <path d="M0 0 H308 V10 L154 58 L0 10Z" fill="var(--brown)"/>
      <path d="M0 10 L154 58 L308 10" stroke="var(--green-dark)" stroke-width="2" fill="none"/>
      <path d="M0 113 L140 62 M308 113 L168 62" stroke="#ddd" stroke-width="1"/>
      <path d="M0 98 Q154 80 308 94 V113 H0Z" fill="var(--green)"/>
    </svg>
    <div class="wordmark" style="position:absolute;left:50%;top:22px;transform:translateX(-50%);font-size:7px;color:var(--paper)"><span class="mark" style="width:8px;height:8px;background:var(--paper)"></span>Turnip Cuddler</div>
  </section>
  <section class="item envelope-front" style="left:868px;top:197px;width:308px;height:86px">
    <svg class="flap" viewBox="0 0 308 86" preserveAspectRatio="none" style="position:absolute;inset:0;width:100%;height:100%">
      <path d="M0 0 L154 48 L308 0" stroke="#d8d8d8" stroke-width="1.2" fill="none"/>
      <path d="M0 86 L130 44 M308 86 L178 44" stroke="#e2e2e2" stroke-width="1"/>
    </svg>
    <div class="wordmark"><span class="mark"></span>Turnip Cuddler</div>
  </section>

</main>
</body>
</html>
```